Dale Hobbin Book Cover Design Project

I would like a book cover design for a science fiction book tentatively entitled "Quiet Orbit" by Dalton K Hobbin III.

The book opens with a scene in the foothills of the Blue Ridge Valley:

"Riding alone on a crisp December morning, Ned Paxford suddenly and uncharacteristically curses. For the fifth time in as many rides, Paxford’s Plimbo had delivered the same anonymous message—this time paradoxically following The Hollow Pikes’ Lantern on the Weir. The message simply said: “Dr. Paxford, I’m a messenger from God. He has a mission for you. Please meet me at noon on Christmas day in the videoconference room at your school. Come alone. More will be revealed.”

I imagine a cover showing the Blue Ridge Mountains, but could be convince otherwise.

Target Market(s)

Highly educated readers struggling to reconcile science and faith.

Industry/Entity Type

School

Requirements
Must have
• Book Title
Author's Name
Nice to have
• Blue Ridge Mountain scene

```html
<!DOCTYPE html>
<html lang="en">
<head>
<meta charset="utf-8">
<title>Quiet Orbit — Book Cover Wrap</title>
<link rel="stylesheet" href="https://fonts.googleapis.com/css2?family=Cormorant+Garamond:wght@600&family=Oranienbaum&display=swap">
<style>
  :root {
    --sky-blue: #4f7fb0;
    --sky-pale: #b9c9d6;
    --sun-core: #fffbe8;
    --sun-glow: #f3d98a;
    --haze-gold: #c9a667;
    --ridge-brown: #7b6440;
    --rock-dark: #2b2a26;
    --rock-light: #b9b6ad;
    --title-green: #0f5a1f;
    --title-edge: #081a0a;
    --body-ink: #111111;
  }
  * { margin: 0; padding: 0; box-sizing: border-box; }
  html, body { width: 1200px; height: 800px; overflow: hidden; background: #fff; }

  .cover-wrap {
    position: relative;
    width: 1200px;
    height: 800px;
    overflow: hidden;
  }

  .mountain-scene {
    position: absolute;
    inset: 0;
    background:
      radial-gradient(circle at 945px 245px, var(--sun-core) 0, var(--sun-glow) 60px, rgba(243,217,138,0.5) 170px, rgba(243,217,138,0) 340px),
      radial-gradient(ellipse 260px 200px at 120px 560px, rgba(255,240,190,0.75), rgba(255,240,190,0) 100%),
      radial-gradient(ellipse 420px 170px at 760px 720px, var(--rock-light), rgba(185,182,173,0) 100%),
      linear-gradient(180deg,
        var(--sky-blue) 0%,
        var(--sky-pale) 22%,
        #d9cfa8 33%,
        var(--haze-gold) 45%,
        var(--ridge-brown) 62%,
        #5a4a33 78%,
        var(--rock-dark) 100%);
  }

  .back-blurb {
    position: absolute;
    left: 40px;
    top: 8px;
    width: 450px;
    font-family: "Cormorant Garamond", serif;
    font-weight: 600;
    font-size: 17.5px;
    line-height: 35px;
    color: var(--body-ink);
    text-align: center;
  }
  .back-blurb p { white-space: nowrap; }

  .spine-title,
  .front-author,
  .front-title {
    position: absolute;
    overflow: visible;
  }
  .spine-title { left: 560px; top: 0; width: 80px; height: 800px; }
  .front-author { left: 680px; top: 40px; width: 490px; height: 80px; }
  .front-title { left: 680px; top: 350px; width: 510px; height: 440px; }

  .title-type {
    font-family: "Oranienbaum", serif;
    fill: var(--title-green);
    stroke: var(--title-edge);
    stroke-width: 2;
    paint-order: stroke;
    filter: drop-shadow(3px 3px 0 var(--title-edge));
  }
</style>
</head>
<body>
<main class="cover-wrap">
  <div class="mountain-scene" role="img" aria-label="Blue Ridge Mountains at sunrise: golden sun over hazy ridges, blue sky with clouds, pine trees and a frosted rocky outcrop in the foreground"></div>

  <section class="back-blurb">
    <p>Riding alone on a crisp December morning, Ned Paxford</p>
    <p>suddenly and uncharacteristically curses.  For the fifth time</p>
    <p>in as many rides, Paxford’s Plimbo had delivered the same</p>
    <p>anonymous message- this time paradoxically following</p>
    <p>The Hollow Pikes 'Lantern on the Weir'. The message</p>
    <p>simply said "Dr. Paxford. I'm a messenger from God.</p>
    <p>He has a mission for you.  Please meet me at noon on</p>
    <p>Christmas day in the videoconference room at your school.</p>
    <p>Come alone.</p>
    <p>More will be revealed."</p>
  </section>

  <svg class="spine-title" viewBox="0 0 80 800" aria-label="Dalton K Hobbin III — Quiet Orbit">
    <g transform="translate(18 0) rotate(90)">
      <text class="title-type" x="4" y="0" font-size="62" textLength="300" lengthAdjust="spacingAndGlyphs">Dalton K Hobbin III</text>
      <text class="title-type" x="350" y="0" font-size="66" textLength="440" lengthAdjust="spacingAndGlyphs">QUIET ORBIT</text>
    </g>
  </svg>

  <svg class="front-author" viewBox="0 0 490 80">
    <text class="title-type" x="0" y="66" font-size="78" textLength="478" lengthAdjust="spacingAndGlyphs">Dalton K Hobbin III</text>
  </svg>

  <svg class="front-title" viewBox="0 0 510 440">
    <text class="title-type" x="150" y="110" font-size="130" textLength="210" lengthAdjust="spacingAndGlyphs">QUIET</text>
    <text class="title-type" x="10" y="410" font-size="290" textLength="490" lengthAdjust="spacingAndGlyphs">ORBIT</text>
  </svg>
</main>
</body>
</html>
```